General contractor/GM consaltant business card

I need a card for my contracting company in North Dakota, we build industrial buildings for the oil feild and oil feild related companies offices, shops, airplain hangars, airports ext. We have a familly atmosphere on the job and are very relational and personal.
Industry/Entity Type
Industrial
Contact Information for Business Card
Kestrelmoor Builders LLC.
Dwight T.Halvorsun
4736 Quillfern dr. Colorado Springs, CO. 80927
Cell# 406-555-8142
dwight@kestrelmoorbuilders.com

```html
<!DOCTYPE html>
<html lang="en">
<head>
<meta charset="utf-8">
<title>Kestrelmoor Builders LLC. – Business Card</title>
<link href="https://fonts.googleapis.com/css2?family=Michroma&family=Tinos&display=swap" rel="stylesheet">
<style>
  :root {
    --stage: #e4e2df;
    --card-black: #0b0b0c;
    --sky-light: #6a6b6e;
    --sky-mid: #3a3b3e;
    --sky-dark: #141416;
    --brand-blue: #2ba6df;
    --ink-white: #f2f2f2;
    --band-grey: rgba(120, 124, 130, 0.55);
    --night-amber: #c9a43a;
    --night-steel: #4a4e5a;
  }
  * { margin: 0; padding: 0; box-sizing: border-box; }
  html, body { width: 1200px; height: 800px; overflow: hidden; }
  body {
    background: var(--stage);
    display: flex;
    align-items: center;
    justify-content: center;
    gap: 40px;
  }
  .card {
    position: relative;
    width: 525px;
    height: 300px;
    overflow: hidden;
    background: var(--card-black);
    box-shadow: 0 10px 28px rgba(0,0,0,0.28);
  }
  .brand-name {
    font-family: "Michroma", sans-serif;
    font-variant: small-caps;
    color: var(--brand-blue);
    letter-spacing: 0.06em;
    white-space: nowrap;
  }

  /* Contact side */
  .card--contact .site-photo {
    position: absolute; inset: 0;
    background:
      linear-gradient(100deg, rgba(5,5,6,0.95) 0%, rgba(10,10,12,0.75) 28%, rgba(0,0,0,0) 48%),
      linear-gradient(180deg, var(--sky-light) 0%, var(--sky-mid) 45%, var(--sky-dark) 100%);
  }
  .card--contact .top-band {
    position: absolute; left: 0; right: 0; top: 0; height: 62px;
    background: linear-gradient(180deg, rgba(0,0,0,0.55), rgba(0,0,0,0.15));
  }
  .card--contact .brand-name {
    position: absolute; left: 20px; top: 22px;
    font-size: 19px;
  }
  .contact-list {
    position: absolute; right: 26px; top: 74px;
    list-style: none;
    text-align: right;
    font-family: "Tinos", serif;
    color: var(--ink-white);
    font-size: 15px;
    line-height: 34px;
  }
  .contact-list .address { font-size: 16px; }

  /* Front side */
  .card--front .night-photo {
    position: absolute; left: 0; right: 0; top: 62px; bottom: 0;
    background:
      radial-gradient(ellipse 40% 35% at 30% 85%, rgba(201,164,58,0.55), transparent 70%),
      radial-gradient(ellipse 25% 45% at 78% 55%, rgba(201,164,58,0.35), transparent 70%),
      radial-gradient(ellipse 30% 40% at 55% 70%, rgba(74,78,90,0.9), transparent 75%),
      linear-gradient(180deg, #0a0a0c 0%, #121216 60%, #1a1812 100%);
  }
  .card--front .name-band {
    position: absolute; left: 0; right: 0; top: 108px; height: 64px;
    background: linear-gradient(90deg, var(--band-grey), rgba(60,62,68,0.35));
    padding: 12px 0 0 28px;
  }
  .card--front .brand-name { font-size: 20px; display: block; }
  .card--front .address-line {
    display: block;
    margin-top: 6px;
    font-family: "Michroma", sans-serif;
    font-variant: small-caps;
    color: var(--ink-white);
    font-size: 11px;
    letter-spacing: 0.08em;
    white-space: nowrap;
  }
</style>
</head>
<body>
  <article class="card card--contact">
    <div class="site-photo" role="img" aria-label="Black and white photo of a building under construction with a tower crane against a cloudy sky"></div>
    <div class="top-band"></div>
    <h1 class="brand-name">Kestrelmoor Builders LLC.</h1>
    <ul class="contact-list">
      <li class="person">Dwight T.Halvorsun</li>
      <li class="phone">Cell-406-555-8142</li>
      <li class="email">dwight@kestrelmoorbuilders.com</li>
      <li class="address">4736 Quillfern dr. Colorado Springs, CO. 80927</li>
    </ul>
  </article>

  <article class="card card--front">
    <div class="night-photo" role="img" aria-label="Industrial plant at night with lit towers and storage tanks glowing yellow"></div>
    <div class="name-band">
      <h2 class="brand-name">Kestrelmoor Builders LLC.</h2>
      <span class="address-line">Quillfern dr. Colorado Springs, CO. 80927</span>
    </div>
  </article>
</body>
</html>
```